Lantern of Renewal needs a business card design

I need a business card design for my company to promote my new Christian non-fiction book, "Where The River Bends Home." I also want it to promote my web site, www.lanternofrenewalbks.com. The book is about empowering people to be transformed through a deeper relationship with God. I am picturing a design with a dove over water that matches the colors of my book cover, blue, white, yellow, and orange. Fire and light would also be possible elements of the design. I would like to be able to use the dove by itself as a logo for my business. This is my first book and I do not know if others will follow. The name of my publishing company is Silver Harvest Press, named after Gideon in the Bible story from the book of Judges. My book was independently published and was recently selected as a finalist for the 2015 Bright Horizon SMALLPRESS book award in the Christian non-fiction genre.

Target Market(s)

People who are hungry for more of God and who want to experience deep change in their lives.

Industry/Entity Type

Business

Contact Information for Business Card

Dana Whitcombe
Author
Where The River Bends Home
4287 Maple Orchard Lane
Austin, Texas 78651-2097
512-555-0143 512-555-0178
dana-whitcombe@examplemail.net
www.lanternofrenewalbks.com

Colors
0355a3
3377b5
85acd3
cedeed
fbee3e
ffc214

Requirements
Must have
• A dove with a blue background, peaceful and appealing
Nice to have
• Water and fire or light
Should not have
• Violence or fear-producing images

```html
<!DOCTYPE html>
<html lang="en">
<head>
<meta charset="utf-8">
<title>Dana Whitcombe – Business Card</title>
<link rel="stylesheet" href="https://fonts.googleapis.com/css2?family=Tinos:wght@400;700&family=Pinyon+Script&display=swap">
<style>
  :root {
    --page: #eceeee;
    --sky: #1c86c8;
    --deep: #0a3f93;
    --navy: #08164f;
    --white: #ffffff;
    --gold: #ffc214;
    --band: rgba(20, 40, 90, 0.45);
    --dove-light: #cedeed;
    --dove-mid: #85acd3;
  }
  * { margin: 0; padding: 0; box-sizing: border-box; }
  html, body {
    width: 900px; height: 1200px; overflow: hidden;
    background: var(--page);
  }
  .card {
    position: absolute; left: 120px; top: 40px;
    width: 660px; height: 1120px; overflow: hidden;
    background:
      radial-gradient(ellipse 70% 30% at 40% 38%, rgba(133,172,211,0.35), transparent 70%),
      radial-gradient(ellipse 80% 25% at 50% 70%, rgba(51,119,181,0.35), transparent 70%),
      linear-gradient(160deg, var(--sky) 0%, var(--deep) 38%, #0c3a8c 60%, var(--navy) 100%);
    font-family: "Tinos", "Times New Roman", serif;
    color: var(--white);
  }
  .title {
    position: absolute; left: 0; right: 0; top: 80px;
    text-align: center;
  }
  .title-line {
    display: block;
    font-weight: 700; font-size: 70px; line-height: 73px;
    letter-spacing: 6px;
  }
  .title-script {
    display: block; margin-top: 8px;
    font-family: "Pinyon Script", cursive;
    font-size: 66px; line-height: 80px;
    color: var(--gold);
  }
  .name-band {
    position: absolute; left: 0; right: 0; top: 490px; height: 124px;
    background: var(--band);
    text-align: center;
    z-index: 2;
  }
  .author-name { font-weight: 700; font-size: 38px; margin-top: 22px; line-height: 46px; }
  .author-role { font-size: 34px; line-height: 40px; }
  .dove {
    position: absolute; left: 250px; top: 626px; width: 380px; height: 160px;
    border-radius: 50%;
    background: radial-gradient(ellipse at 50% 45%, var(--white) 0%, var(--dove-light) 45%, rgba(133,172,211,0.4) 75%, transparent 100%);
    z-index: 1;
  }
  .contact {
    position: absolute; left: 72px; top: 790px; list-style: none;
    z-index: 2;
  }
  .contact li {
    display: flex; align-items: flex-start;
    font-size: 31px; line-height: 46px; margin-bottom: 2px;
  }
  .contact svg { width: 28px; height: 28px; margin: 9px 12px 0 0; flex: none; }
</style>
</head>
<body>
  <div class="card">
    <h1 class="title">
      <span class="title-line">WHERE</span>
      <span class="title-line">THE</span>
      <span class="title-line">RIVER</span>
      <span class="title-line">BENDS</span>
      <span class="title-script">Home</span>
    </h1>

    <div class="name-band">
      <p class="author-name">Dana Whitcombe</p>
      <p class="author-role">Author</p>
    </div>

    <div class="dove" role="img" aria-label="White dove in flight carrying an olive branch"></div>

    <ul class="contact">
      <li>
        <svg viewBox="0 0 24 24" fill="none" stroke="#fff" stroke-width="2"><path d="M5 3h4l2 5-2.5 1.5a11 11 0 0 0 6 6L16 13l5 2v4a2 2 0 0 1-2 2A16 16 0 0 1 3 5a2 2 0 0 1 2-2z"/></svg>
        512-555-0143
      </li>
      <li>
        <svg viewBox="0 0 24 24" fill="none" stroke="#fff" stroke-width="2"><rect x="6" y="2" width="12" height="20" rx="2"/><line x1="10" y1="18" x2="14" y2="18"/></svg>
        512-555-0178
      </li>
      <li>
        <svg viewBox="0 0 24 24" fill="none" stroke="#fff" stroke-width="2"><rect x="2" y="5" width="20" height="14" rx="1"/><path d="M2 6l10 7 10-7"/></svg>
        dana-whitcombe@examplemail.net
      </li>
      <li>
        <svg viewBox="0 0 24 24" fill="none" stroke="#fff" stroke-width="1.8"><circle cx="12" cy="12" r="10"/><ellipse cx="12" cy="12" rx="4.5" ry="10"/><line x1="2" y1="12" x2="22" y2="12"/><path d="M4 7h16M4 17h16"/></svg>
        www.lanternofrenewalbks.com
      </li>
      <li>
        <svg viewBox="0 0 24 24" fill="#fff"><path d="M12 2L1 9h22z"/><rect x="3" y="11" width="18" height="2"/><rect x="4" y="14" width="4" height="7"/><rect x="10" y="14" width="4" height="7"/><rect x="16" y="14" width="4" height="7"/></svg>
        <span>4287 Maple Orchard Lane Austin,<br>Texas&nbsp; 78651-2097</span>
      </li>
    </ul>
  </div>
</body>
</html>
```